KLMR stationery 2023

Our stationery dates back to 2007 when we changed practice rooms.
We would like to have kept the logo and spiced up the design, especially since we have one more colleague (Dr. Henriette Bollmeyer)
Our practice colors are a slightly more muted pink and sand-colored.
Follow-up orders for flyers, notices, etc. are still waiting for this design.

```html
<!DOCTYPE html>
<html lang="de">
<head>
<meta charset="utf-8">
<title>KLMR Briefpapier</title>
<link href="https://fonts.googleapis.com/css2?family=PT+Sans+Narrow:wght@400;700&display=swap" rel="stylesheet">
<style>
  :root {
    --backdrop: #3b1330;
    --paper: #ffffff;
    --pink: #b963a5;
    --pink-soft: #b274ae;
    --sand: #e8c472;
    --sand-dark: #b58d6a;
    --ink: #1c1c1c;
    --ink-soft: #2b2b2b;
  }
  * { margin: 0; padding: 0; box-sizing: border-box; }
  html, body { width: 1200px; height: 1200px; overflow: hidden; }
  body {
    background: var(--backdrop);
    font-family: "PT Sans Narrow", "Arial Narrow", sans-serif;
    position: relative;
  }
  .letterhead {
    position: absolute;
    left: 204px; top: 45px;
    width: 791px; height: 1110px;
    background: var(--paper);
    box-shadow: 0 4px 18px rgba(0,0,0,.45);
    overflow: hidden;
  }
  .header-decor {
    position: absolute; left: 172px; top: 0;
    width: 619px; height: 238px;
    background: linear-gradient(160deg, var(--pink) 0%, var(--pink-soft) 55%, var(--sand) 100%);
    border-bottom-left-radius: 100% 100%;
  }
  .brand {
    position: absolute; left: 26px; top: 86px;
    display: flex; align-items: center; gap: 14px;
  }
  .brand-dot { width: 34px; height: 34px; border-radius: 50%; background: var(--pink); }
  .brand-name {
    font-size: 92px; font-weight: 400; color: var(--ink);
    letter-spacing: 3px; line-height: 1;
  }
  .doctor-band {
    position: absolute; left: 0; top: 941px; width: 100%; height: 25px;
    background: var(--pink);
    border-top: 3px solid #e7d3e4;
    display: flex; align-items: center; justify-content: space-between;
    padding: 0 28px 0 30px;
    color: #fff; font-size: 16px;
  }
  .doctor-band li { list-style: none; display: flex; align-items: center; gap: 7px; }
  .doctor-band li::before {
    content: ""; width: 5px; height: 5px; border-radius: 50%; background: #fff;
  }
  .info-panel {
    position: absolute; left: 0; top: 966px; width: 100%; height: 144px;
    background: var(--sand);
  }
  .practice-illustration {
    position: absolute; left: 27px; top: 8px; width: 206px; height: 118px;
    background: linear-gradient(100deg, rgba(255,255,255,.75), rgba(255,255,255,.35));
    border-radius: 4px;
  }
  .services {
    position: absolute; left: 253px; top: 13px; width: 520px;
    display: grid; grid-template-columns: 226px 143px 1fr; row-gap: 4px;
    font-size: 13.5px; color: var(--ink-soft);
  }
  .services li { list-style: none; display: flex; align-items: center; gap: 6px; white-space: nowrap; }
  .tick { width: 14px; height: 14px; flex: none; }
  .divider {
    position: absolute; left: 254px; top: 58px; width: 516px; height: 1px; background: var(--pink);
  }
  .contacts {
    position: absolute; left: 254px; top: 68px; width: 520px;
    display: grid; grid-template-columns: 188px 177px 1fr;
    font-size: 12.5px; color: var(--ink-soft); line-height: 18px;
  }
  .contact-item { display: flex; gap: 6px; white-space: nowrap; }
  .contact-icon { width: 14px; height: 14px; flex: none; margin-top: 2px; }
  .hours {
    position: absolute; left: 255px; top: 106px;
    font-size: 12.5px; color: var(--ink-soft);
  }
  .hours .label { color: var(--pink); font-weight: 700; margin-right: 8px; }
  .hours strong { font-weight: 700; }
</style>
</head>
<body>
  <main class="letterhead">
    <div class="header-decor" role="img" aria-label="Dekorative Welle in Rosa und Sandfarbe"></div>

    <div class="brand">
      <span class="brand-dot"></span>
      <span class="brand-name">KLMR</span>
    </div>

    <ul class="doctor-band">
      <li>Dr. Gisela Marthaler</li>
      <li>Dr. Petra Lindqvist</li>
      <li>Dr. Lukas Marthaler</li>
      <li>Dr. Ilona Varga</li>
      <li>Dr. Henriette Bollmeyer</li>
    </ul>

    <section class="info-panel">
      <div class="practice-illustration" role="img" aria-label="Illustration: Frauen-Silhouetten vor dem Praxisgebäude"></div>

      <ul class="services">
        <li><svg class="tick" viewBox="0 0 14 14"><circle cx="7" cy="7" r="7" fill="var(--pink)"/><path d="M3.8 7.2l2.2 2.2 4.2-4.6" stroke="#fff" stroke-width="1.8" fill="none"/></svg>Fachärzte für Gynäkologie und Geburtshilfe</li>
        <li><svg class="tick" viewBox="0 0 14 14"><circle cx="7" cy="7" r="7" fill="var(--pink)"/><path d="M3.8 7.2l2.2 2.2 4.2-4.6" stroke="#fff" stroke-width="1.8" fill="none"/></svg>Pränataldiagnostik</li>
        <li><svg class="tick" viewBox="0 0 14 14"><circle cx="7" cy="7" r="7" fill="var(--pink)"/><path d="M3.8 7.2l2.2 2.2 4.2-4.6" stroke="#fff" stroke-width="1.8" fill="none"/></svg>Schwangerschaftsbetreuung</li>
        <li><svg class="tick" viewBox="0 0 14 14"><circle cx="7" cy="7" r="7" fill="var(--pink)"/><path d="M3.8 7.2l2.2 2.2 4.2-4.6" stroke="#fff" stroke-width="1.8" fill="none"/></svg>Kinderwunschbehandlung</li>
        <li><svg class="tick" viewBox="0 0 14 14"><circle cx="7" cy="7" r="7" fill="var(--pink)"/><path d="M3.8 7.2l2.2 2.2 4.2-4.6" stroke="#fff" stroke-width="1.8" fill="none"/></svg>Ambulante Operationen</li>
        <li><svg class="tick" viewBox="0 0 14 14"><circle cx="7" cy="7" r="7" fill="var(--pink)"/><path d="M3.8 7.2l2.2 2.2 4.2-4.6" stroke="#fff" stroke-width="1.8" fill="none"/></svg>Onkologische Betreuung</li>
      </ul>

      <div class="divider"></div>

      <div class="contacts">
        <div class="contact-item">
          <svg class="contact-icon" viewBox="0 0 14 14"><circle cx="7" cy="7" r="6.3" fill="none" stroke="var(--pink)"/><circle cx="7" cy="6" r="2" fill="none" stroke="var(--pink)"/><path d="M4 10.5h6" stroke="var(--pink)"/></svg>
          <div>Ahornweg 14<br>8400 Talwil</div>
        </div>
        <div>
          <div class="contact-item"><svg class="contact-icon" viewBox="0 0 14 14"><circle cx="7" cy="7" r="6.3" fill="none" stroke="var(--pink)"/><path d="M4.5 4.5c0 3 2 5 5 5l.6-1.3-1.5-.8-.7.7c-.9-.4-1.6-1.1-2-2l.7-.7-.8-1.5z" fill="var(--pink)"/></svg>052 / 418 26 90</div>
          <div class="contact-item"><svg class="contact-icon" viewBox="0 0 14 14"><circle cx="7" cy="7" r="6.3" fill="none" stroke="var(--pink)"/><rect x="4.2" y="5" width="5.6" height="4.5" fill="none" stroke="var(--pink)"/></svg>052 / 418 26 91</div>
        </div>
        <div>
          <div class="contact-item"><svg class="contact-icon" viewBox="0 0 14 14"><circle cx="7" cy="7" r="6.3" fill="none" stroke="var(--pink)"/><rect x="4" y="5" width="6" height="4.2" fill="none" stroke="var(--pink)"/><path d="M4 5l3 2.4L10 5" fill="none" stroke="var(--pink)"/></svg>praxis@klmr-aerzte.ch</div>
          <div class="contact-item"><svg class="contact-icon" viewBox="0 0 14 14"><circle cx="7" cy="7" r="6.3" fill="none" stroke="var(--pink)"/><circle cx="7" cy="7" r="3" fill="none" stroke="var(--pink)"/><path d="M4 7h6M7 4v6" stroke="var(--pink)"/></svg>www.klmr-aerzte.ch</div>
        </div>
      </div>

      <p class="hours"><span class="label">Öffnungszeiten NEU:</span>Montag - Freitag <strong>08.00 - 12.00 Uhr</strong> und <strong>13.00 - 17.00 Uhr</strong></p>
    </section>
  </main>
</body>
</html>
```